Design Business Cards

I need a new business card designed in two versions, one an International version and one a Japanese version.

Please ensure to submit designer files so we can edit it ourselves after the contest. We require the following file formats at minimum (AI, PSD, PNG).

I have attached 4 examples of letterpress business cards and the kind of style we want. Below you will find all the data for the front and back of the two cards, please come up with your own layout for how you think it should be best presented based on the data below, brief and examples.

I have also attached our company logo file.

Design Brief:

Simple and elegant business card, white, two sided. We will be producing two versions an international version and a Japanese version. We will require finished designs for both. These will be printed via letterpress and this should be considered when creating the design.

The (text) indicates what the information is and should not appear on the design. This is just for your reference.

International Front:

Company Logo

International Back:

Company Logo

Desmond Hartwick (Name)
Commercial Manager (Title)
+61 455 287 913 (Telephone)
randall@[login to view URL] (Email)

2078/4 Larkspur Rd
Melbourne, Vic, 3004
Australia
(Address)

United Kingdom | Australia | Hong Kong
(Worldwide Office Locations)

Japanese Front:

Company Logo

Desmond Hartwick (Name)
コマーシャルマネージャー (Title)

2078/4 Larkspur Rd
Melbourne, Vic, 3004
Australia
(Address)

イギリス|オーストラリア|香港

Japanese Back:

Company Logo

Desmond Hartwick (Name)

2078/4 Larkspur Rd
Melbourne, Vic, 3004
Australia
(Address)

```html
<!DOCTYPE html>
<html lang="en">
<head>
<meta charset="utf-8">
<title>Halden Events – Business Cards</title>
<link href="https://fonts.googleapis.com/css2?family=Lato:wght@400;700&display=swap" rel="stylesheet">
<style>
  :root {
    --backdrop: #b3b5b8;
    --card: #f7f6f2;
    --card-edge: #e4e1d8;
    --brand-blue: #1e8ec0;
    --ink: #1f1f1f;
    --ink-soft: #3a3a3a;
  }
  * { margin: 0; padding: 0; box-sizing: border-box; }
  html, body {
    width: 1200px;
    height: 1049px;
    overflow: hidden;
    background: var(--backdrop);
    font-family: "Lato", sans-serif;
  }
  .canvas {
    position: relative;
    width: 1200px;
    height: 1049px;
  }
  .card {
    position: absolute;
    width: 560px;
    height: 340px;
    background: var(--card);
    border: 1px solid var(--card-edge);
  }
  .card--front { left: 560px; top: 110px; }
  .card--back  { left: 90px;  top: 560px; }

  .brand-name {
    color: var(--brand-blue);
    font-weight: 700;
    letter-spacing: 0.04em;
    line-height: 1;
    white-space: nowrap;
  }
  .card--front .brand-name {
    position: absolute;
    left: 0; right: 0;
    top: 118px;
    text-align: center;
    font-size: 50px;
  }
  .office-locations {
    position: absolute;
    left: 0; right: 0;
    top: 206px;
    text-align: center;
    font-size: 15px;
    color: var(--ink-soft);
    letter-spacing: 0.02em;
  }
  .card--back .brand-name {
    position: absolute;
    left: 36px;
    top: 36px;
    font-size: 28px;
  }
  .address {
    position: absolute;
    left: 36px;
    top: 168px;
    font-size: 13px;
    line-height: 1.35;
    color: var(--ink-soft);
  }
  .contact-person {
    position: absolute;
    right: 36px;
    top: 196px;
    text-align: right;
  }
  .contact-person__name {
    font-size: 19px;
    font-weight: 700;
    color: var(--ink);
  }
  .contact-person__title {
    font-size: 13px;
    color: var(--ink-soft);
    margin-top: 2px;
  }
  .contact-list {
    position: absolute;
    right: 36px;
    bottom: 26px;
    list-style: none;
    font-size: 12.5px;
    color: var(--ink-soft);
  }
  .contact-list li {
    display: flex;
    justify-content: flex-end;
    align-items: center;
    gap: 8px;
    line-height: 1.55;
  }
  .contact-list svg {
    width: 11px;
    height: 11px;
    fill: var(--ink);
  }
</style>
</head>
<body>
<main class="canvas">

  <section class="card card--front" aria-label="Card front">
    <div class="brand-name">Halden Events</div>
    <p class="office-locations">United Kingdom | Australia | Hong Kong</p>
  </section>

  <section class="card card--back" aria-label="Card back">
    <div class="brand-name">Halden Events</div>

    <address class="address" style="font-style: normal;">
      2078/4 Larkspur Rd<br>
      Melbourne, Vic, 3004<br>
      Australia
    </address>

    <div class="contact-person">
      <div class="contact-person__name">Desmond Hartwick</div>
      <div class="contact-person__title">Commercial Manager</div>
    </div>

    <ul class="contact-list">
      <li>+61 455 287 913
        <svg viewBox="0 0 24 24" aria-hidden="true"><path d="M6.6 10.8a15.1 15.1 0 0 0 6.6 6.6l2.2-2.2a1 1 0 0 1 1-.25 11.4 11.4 0 0 0 3.6.57 1 1 0 0 1 1 1V20a1 1 0 0 1-1 1A17 17 0 0 1 3 4a1 1 0 0 1 1-1h3.5a1 1 0 0 1 1 1c0 1.25.2 2.45.57 3.57a1 1 0 0 1-.25 1z"/></svg>
      </li>
      <li>desmond@haldenevents.com
        <svg viewBox="0 0 24 24" aria-hidden="true"><path d="M2 5h20v14H2z M4 7v.5l8 5 8-5V7l-8 5z" fill-rule="evenodd"/></svg>
      </li>
      <li>www.haldenevents.com
        <svg viewBox="0 0 24 24" aria-hidden="true"><circle cx="12" cy="12" r="10"/><path d="M2 12h20M12 2c3 3 3 17 0 20M12 2c-3 3-3 17 0 20" stroke="#f7f6f2" stroke-width="1.6" fill="none"/></svg>
      </li>
    </ul>
  </section>

</main>
</body>
</html>
```